BLUE FORGE (Business Card for Training Company)

Blue Forge is a training and consultancy company with a focus on executive protection and medical. I would like the card to be nice and sharp, not overdone and in black and red. I would also like it to highlight that it is "A Tavmont Company"

I would like it to be simple and highlight a few things.

1. Name
2. Title
3. Phone Number
4. Email

I would also like www.tavmontgroup.example/blue-forge to be on the card somewhere.

Target Market(s)

Security Companies

Industry/Entity Type

Security

Contact Information for Business Card

Blue Forge is a training and consultancy company with a focus on executive protection and medical. I would like the card to be nice and sharp, not overdone and in black and red. I would also like it to highlight that it is "A Tavmont Company" I would like it to be simple and highlight a few things. 1. Name 2. Title 3. Phone Number 4. Email I would also like www.tavmontgroup.example/blue-forge to be on the card somewhere.

Requirements
Must have
• A Tavmont Company listed on the card and the website
Nice to have
• Highlight Medical Training, Consultancy & Executive Protection Courses

```html
<!DOCTYPE html>
<html lang="en">
<head>
<meta charset="utf-8">
<title>Blue Forge – Business Card</title>
<link rel="stylesheet" href="https://fonts.googleapis.com/css2?family=Roboto:wght@400;500;700&family=Playfair+Display:wght@700&display=swap">
<style>
  :root {
    --ink: #060807;
    --paper: #ffffff;
    --crimson: #7b0000;
    --crimson-dark: #5c0a0a;
    --backdrop: #c4b9b9;
    --text-light: #ffffff;
  }
  * { margin: 0; padding: 0; box-sizing: border-box; }
  html, body {
    width: 1200px; height: 960px; overflow: hidden;
    background: var(--backdrop);
    font-family: "Roboto", Arial, sans-serif;
  }
  .canvas { position: relative; width: 1200px; height: 960px; }

  .card { position: absolute; overflow: hidden; background: var(--ink); }

  /* Front card */
  .card--front { left: 257px; top: 46px; width: 673px; height: 385px; }
  .front__panel {
    position: absolute; left: 17px; top: 0; width: 278px; height: 100%;
    background: var(--paper);
  }
  .front__divider {
    position: absolute; left: 295px; top: 0; width: 5px; height: 100%;
    background: var(--crimson);
  }
  .front__edge-bar {
    position: absolute; left: 0; top: 94px; width: 18px; height: 215px;
    background: var(--crimson);
  }
  .front__edge-line {
    position: absolute; left: 18px; top: 94px; width: 7px; height: 215px;
    background: var(--ink);
  }
  .wordmark {
    position: absolute; font-weight: 700; line-height: 0.86;
    letter-spacing: 1px; text-transform: uppercase;
  }
  .front .wordmark,
  .card--front .wordmark {
    left: 66px; top: 172px; font-size: 42px; color: var(--crimson-dark);
  }
  .holder { position: absolute; left: 336px; top: 55px; }
  .holder__name {
    font-size: 21px; font-weight: 700; color: var(--text-light); letter-spacing: 0.6px;
  }
  .holder__title {
    margin-top: 6px; font-size: 15px; font-weight: 400; color: var(--crimson);
  }
  .contact {
    position: absolute; left: 286px; width: 387px; height: 36px;
    background: var(--crimson); display: flex; align-items: center;
    color: var(--text-light); font-size: 15px;
  }
  .contact--phone { top: 175px; }
  .contact--email { top: 226px; }
  .contact--web { top: 277px; }
  .contact__icon { width: 22px; height: 22px; margin-left: 21px; margin-right: 11px; flex: none; }

  /* Back card */
  .card--back { left: 257px; top: 507px; width: 669px; height: 382px; }
  .back__drop { position: absolute; left: 322px; top: 0; width: 26px; height: 39px; }
  .card--back .wordmark {
    left: 0; width: 100%; text-align: center; top: 123px;
    font-size: 42px; color: var(--text-light);
  }
  .back__parent {
    position: absolute; left: 0; width: 100%; top: 290px; text-align: center;
    font-family: "Playfair Display", Georgia, serif; font-weight: 700;
    font-size: 15px; color: var(--text-light);
  }
  .back__services {
    position: absolute; left: 0; bottom: 0; width: 100%; height: 44px;
    background: var(--crimson); color: var(--ink);
    font-size: 17px; text-align: center; padding-top: 4px;
  }
</style>
</head>
<body>
<main class="canvas">

  <section class="card card--front" aria-label="Business card front">
    <div class="front__panel"></div>
    <div class="front__divider"></div>
    <div class="front__edge-bar"></div>
    <div class="front__edge-line"></div>
    <div class="wordmark">Blue<br>Forge</div>

    <div class="holder">
      <p class="holder__name">MORGAN HALE</p>
      <p class="holder__title">Director</p>
    </div>

    <div class="contact contact--phone">
      <svg class="contact__icon" viewBox="0 0 22 22" aria-hidden="true">
        <circle cx="11" cy="11" r="11" fill="#060807"/>
        <rect x="7.5" y="4.5" width="7" height="13" rx="1.2" fill="none" stroke="#fff" stroke-width="1.4"/>
        <circle cx="11" cy="15.3" r="0.8" fill="#fff"/>
      </svg>
      <span>+ (61) 555 010 234</span>
    </div>
    <div class="contact contact--email">
      <svg class="contact__icon" viewBox="0 0 22 22" aria-hidden="true">
        <circle cx="11" cy="11" r="11" fill="#060807"/>
        <text x="11" y="15.5" text-anchor="middle" font-family="Roboto, Arial, sans-serif" font-size="14" font-weight="700" fill="#fff">@</text>
      </svg>
      <span>info@tavmontgroup.example</span>
    </div>
    <div class="contact contact--web">
      <svg class="contact__icon" viewBox="0 0 22 22" aria-hidden="true">
        <circle cx="11" cy="11" r="11" fill="#060807"/>
        <g fill="none" stroke="#fff" stroke-width="1">
          <circle cx="11" cy="11" r="5.5"/>
          <ellipse cx="11" cy="11" rx="2.4" ry="5.5"/>
          <line x1="5.5" y1="11" x2="16.5" y2="11"/>
          <line x1="6.3" y1="8.3" x2="15.7" y2="8.3"/>
          <line x1="6.3" y1="13.7" x2="15.7" y2="13.7"/>
        </g>
      </svg>
      <span>www.tavmontgroup.example/blue-forge</span>
    </div>
  </section>

  <section class="card card--back" aria-label="Business card back">
    <svg class="back__drop" viewBox="0 0 26 39" aria-hidden="true">
      <path d="M0 0 H26 V14 C26 28 19 39 13 39 C7 39 0 28 0 14 Z" fill="#7b0000"/>
    </svg>
    <div class="wordmark">Blue<br>Forge</div>
    <p class="back__parent">A Tavmont Company</p>
    <p class="back__services">Medical Training | Consultancy | Executive Protection Courses</p>
  </section>

</main>
</body>
</html>
```